Seller's Experience Guide Book

Hello!

This is a seller experience guide book for my real estate company Marlowquist Realty. This will be given to clients and customized per client but we needed a base template. Please use the highlighted yellow text as direction and please keep the content in there per page. This should incorporate our photos where you think our appropriate and our logo. Please use our brand colors. Please use photos of Boston too. Please reach out with questions, future work will be given to the chosen designer. Our brand is luxurious high end and old money looking. Please make this a canvas editable document.

```html
<!DOCTYPE html>
<html lang="en">
<head>
<meta charset="utf-8">
<title>The Marlowquist Seller Experience</title>
<link rel="stylesheet" href="https://fonts.googleapis.com/css2?family=Roboto+Condensed:wght@400;700&family=Arimo:wght@400&display=swap">
<style>
  :root {
    --backdrop: #e4e4e4;
    --paper: #ffffff;
    --gold: #e8b563;
    --navy: #233452;
    --ink: #2b2b2b;
    --wash: #e6e9f2;
  }
  * { box-sizing: border-box; margin: 0; padding: 0; }
  html, body { width: 879px; height: 1200px; overflow: hidden; }
  body { background: var(--backdrop); position: relative; font-family: "Arimo", Arial, sans-serif; }

  .page { position: absolute; background: var(--paper); overflow: hidden; }

  /* Cover */
  .cover { left: 260px; top: 64px; width: 360px; height: 508px; background: var(--gold); }
  .cover-photo {
    position: absolute; left: 0; top: 0; width: 360px; height: 288px;
    background: linear-gradient(180deg, #7fa7d8 0%, #b9c8dc 24%, #d9d2c6 45%, #cfc6b8 65%, #6b6a70 86%, #2c2d33 100%);
  }
  .brand { position: absolute; left: 0; width: 100%; text-align: center; }
  .brand-mark { display: block; margin: 0 auto; width: 40px; height: 40px; border: 2px solid var(--navy); border-radius: 50%; }
  .brand-name {
    display: block; margin-top: 6px; font-family: "Roboto Condensed", Arial, sans-serif; font-weight: 400;
    font-size: 14px; letter-spacing: 0.6px; text-transform: uppercase; color: var(--navy);
  }
  .cover .brand { top: 312px; }
  .cover-title {
    position: absolute; top: 430px; left: 0; width: 100%; text-align: center;
    font-family: "Roboto Condensed", Arial, sans-serif; color: var(--navy);
  }
  .cover-title h1 { font-size: 30px; font-weight: 700; line-height: 32px; }
  .cover-title p { font-size: 15.5px; line-height: 18px; }
  .cover-band {
    position: absolute; left: 0; top: 520px; width: 100%; height: 25px; background: var(--navy);
    color: #fff; font-family: "Roboto Condensed", Arial, sans-serif; font-size: 16px; line-height: 25px; text-align: center;
  }
  .cover-band { top: 456px; }
  .cover-title { top: 394px; }
  .cover .brand { top: 312px; }

  /* Letters */
  .letter { top: 611px; width: 360px; height: 508px; }
  .letter-left { left: 60px; }
  .letter-right { left: 460px; }
  .letter .brand { top: 34px; }
  .letter .brand-mark { width: 36px; height: 36px; }
  .letter .brand-name { font-size: 12.5px; margin-top: 5px; }
  .letter-wash {
    position: absolute; right: 0; bottom: 0; width: 230px; height: 260px;
    background: radial-gradient(ellipse at 80% 75%, var(--wash) 0%, rgba(230,233,242,0.5) 45%, rgba(255,255,255,0) 75%);
  }
  .letter-body {
    position: absolute; left: 31px; top: 114px; width: 295px;
    font-size: 5.6px; line-height: 8.9px; color: var(--ink);
  }
  .letter-body p { margin-bottom: 9px; }
  .letter-body .u { text-decoration: underline; }
  .letter-body ul { list-style: none; }
  .letter-body .l1 { padding-left: 18px; }
  .letter-body .l2 { padding-left: 28px; }
  .letter-body .l3 { padding-left: 37px; }
  .letter-body .tight { margin-bottom: 0; }
</style>
</head>
<body>

<section class="page cover">
  <div class="cover-photo" role="img" aria-label="Photograph of a row of ornate Boston brownstone townhouses behind an iron fence, bare tree branches against a blue sky"></div>
  <div class="brand">
    <span class="brand-mark"></span>
    <span class="brand-name">Marlowquist Realty</span>
  </div>
  <div class="cover-title">
    <h1>48 Linden Court</h1>
    <p>Dorchester, MA 02124</p>
  </div>
  <div class="cover-band">The Marlowquist Seller Experience</div>
</section>

<section class="page letter letter-left">
  <div class="letter-wash" role="img" aria-label="Soft pale blue decorative texture"></div>
  <div class="brand">
    <span class="brand-mark"></span>
    <span class="brand-name">Marlowquist Realty</span>
  </div>
  <div class="letter-body">
    <p>XXX</p>
    <p>Dear XXX</p>
    <p>It was such a pleasure meeting both of you yesterday! I appreciate the time that you spent with me! Since our meeting, I have spent several hours working on a valuation for your beautiful home and looked at it from multiple perspectives.</p>
    <p>In summary, I think the Fair Market Value for the property is $ XXX</p>
    <p>This number was arrived at by looking at all XXX properties sold within the last six, then twelve months, all active listings in XXX, all XXX sold in the last six then twelve months and then comparing based on size, location and condition. This property is very unique based on the total square footage and the third floor apartment (there are several other assets which I will highlight further in this overview) and required careful and thoughtful consideration in deriving value.</p>
    <p>As mentioned yesterday, the Fair Market Value gives us a starting point for a conversation on list price and that is where the strategy piece comes in. I have attached a Comparative Market Analysis based on one of the iterations above. In that report, you'll notice a suggested list price in the range of $ XXX through $ XXX. The final decision will be yours and I'll offer suggestions on the best strategic approach based on merits of low, "right on" and aspirational list prices.</p>
    <p class="tight u">Assets of your property include:</p>
    <p class="l1">- XXX</p>
    <p class="tight u">Your ideal buyer profile:</p>
    <p class="l1">- XXX</p>
    <p class="tight u">Next steps:</p>
    <ul>
      <li class="l1">- Second meeting</li>
      <li class="l2">o Allows me a chance to continue to get to know your home in greater detail (additional photos, videos)</li>
      <li class="l2">o Discuss Listing Agreement</li>
      <li class="l2">o Walkthrough all of the interior and exterior together to share recommendations for preparation for listing</li>
      <li class="l2">o Determine inclusions/exclusions</li>
      <li class="l2">o Create timeline including:</li>
      <li class="l3">- Physical preparation</li>
      <li class="l3">- Schedule photography, video, drone shots</li>
      <li class="l3">- Listing date, Open Houses, offer deadline (would be a conversation to discuss</li>
    </ul>
  </div>
</section>

<section class="page letter letter-right">
  <div class="letter-wash" role="img" aria-label="Soft pale blue decorative texture"></div>
  <div class="brand">
    <span class="brand-mark"></span>
    <span class="brand-name">Marlowquist Realty</span>
  </div>
  <div class="letter-body">
    <p>As mentioned during our meeting, I work very closely with my colleague, Owen Hartley Mara Vellin who owns Marlowquist Realty (please see www.marlowquistboston.com for more information about our company). In short, you will benefit from the knowledge and expertise of two dedicated and highly passionate agents who constantly go above and beyond to support each of our clients.</p>
    <p>In summary, I know this is a very big decision and one that comes with a myriad of emotions. I also know that you have connections with several agents and I am grateful to be considered to sell your home for you! Please know that if selected, XXX. After meeting you yesterday, I am even more excited by the prospect of working in partnership with you and serving as your trusted advisor throughout the process. My goal is to make this transition as smooth as possible for you and your family!</p>
    <p>Please do not hesitate to reach out with any questions you may have about the CMA, my thoughts above or anything else that you may have on your mind. I am here for you and to be of service to you.</p>
    <p>I look forward to hearing back from you!</p>
    <p>Many thanks,<br>Owen or Mara</p>
  </div>
</section>

</body>
</html>
```